“Bright Tide” Spring Fair Poster

We are putting together a school and community fair. We need a poster designed to advertise the event and give some important information to would be attendees. We’d like the poster graphics to evoke a minimalistic and futuristic aesthetic, be bold, yet fun! We will printing the posters, so we will need for them to be at high resolution and ready to send to print.

Target Market(s)

Students, Parents, and Community members

Industry/Entity Type

School

Font styles to use
Sans Serif

Colors
33a6d7
fabb78
9d9d9d
ffffff
1b1b1b
33b8a4

Requirements
Must have
• Bright Tide
• Birch & Lantern Spring Fair 2018
• Friday, May 18th
• 5:00-9:00pm
• Tickets Will Be Available at Select Pick up & Drop Off Times
• Come Enjoy a Futuristic Evening of Food, Music, Entertainment, & Fun!
Nice to have
• We’d love to see a bold and graphic poster with a futuristic feel!
• See the sample image below from previous event poster and additional images for mood and inspiration. Would love to see metallics (silver or metallic colors)

```html
<!DOCTYPE html>
<html lang="en">
<head>
<meta charset="utf-8">
<title>Bright Tide Spring Fair 2018</title>
<link rel="stylesheet" href="https://fonts.googleapis.com/css2?family=Orbitron:wght@500;700;900&display=swap">
<style>
  :root {
    --space: #050607;
    --glow-teal: #33b8a4;
    --glow-deep: #0f3a30;
    --prism: #000000;
    --ink-white: #ffffff;
    --ink-blue: #33a6d7;
    --metal-light: #d9fff6;
    --metal-mid: #5fe0c4;
    --metal-dark: #1e8a78;
  }
  * { margin: 0; padding: 0; box-sizing: border-box; }
  html, body { width: 900px; height: 1200px; overflow: hidden; background: var(--space); }
  .poster {
    position: relative;
    width: 900px;
    height: 1200px;
    overflow: hidden;
    font-family: "Orbitron", sans-serif;
    text-transform: uppercase;
  }
  .space-backdrop {
    position: absolute; inset: 0;
    background:
      radial-gradient(ellipse 40% 6% at 50% 55%, rgba(120,255,220,0.55), transparent 70%),
      radial-gradient(ellipse 3% 45% at 50% 30%, rgba(140,255,225,0.55), transparent 75%),
      radial-gradient(ellipse 55% 30% at 50% 38%, rgba(51,184,164,0.45), transparent 75%),
      radial-gradient(ellipse 70% 45% at 50% 40%, var(--glow-deep), transparent 80%),
      var(--space);
  }
  .prism { position: absolute; inset: 0; }
  .prism-title {
    position: absolute; left: 0; width: 900px;
    text-align: center;
    font-weight: 700;
    line-height: 1;
    background: linear-gradient(180deg, var(--metal-light) 0%, var(--metal-mid) 45%, var(--metal-dark) 60%, var(--metal-light) 100%);
    -webkit-background-clip: text;
    background-clip: text;
    color: transparent;
  }
  .prism-title--small { top: 330px; font-size: 38px; }
  .prism-title--large { top: 400px; font-size: 76px; font-weight: 900; }
  .prism-title--sub   { top: 505px; font-size: 38px; }
  .prism-title--fair  { top: 580px; font-size: 48px; font-weight: 900; }
  .event-info {
    position: absolute; left: 0; width: 900px; top: 752px;
    text-align: center;
    color: var(--ink-white);
    font-weight: 700;
    font-size: 29px;
    line-height: 38px;
    letter-spacing: 0.5px;
    text-shadow: 0 0 4px var(--ink-blue), 0 0 10px var(--ink-blue);
  }
  .event-info p + p { margin-top: 38px; }
</style>
</head>
<body>
  <main class="poster">
    <div class="space-backdrop" role="img" aria-label="Starry deep space with a teal light burst and glowing grid behind the prism"></div>
    <svg class="prism" width="900" height="1200" viewBox="0 0 900 1200" aria-hidden="true">
      <polygon points="454,206 761,660 150,660" fill="var(--prism)"/>
    </svg>
    <h1>
      <span class="prism-title prism-title--small">Bright</span>
      <span class="prism-title prism-title--large">Tide</span>
      <span class="prism-title prism-title--sub">Birch &amp; Lantern</span>
      <span class="prism-title prism-title--fair">Spring Fair 2018</span>
    </h1>
    <section class="event-info">
      <p>Friday, May 18th<br>5:00-9:00 PM</p>
      <p>Tickets will be available at:<br>Select pick up &amp; drop off times</p>
      <p>Come enjoy a futuristic evening<br>of food, music, fun!</p>
    </section>
  </main>
</body>
</html>
```